Enhance the web site presence of KRU Global Limited

Upgrade the current web site www.krucircuit-example.com to share with the audience our current plan and future developments of our company. I have created a worksheet which shows all the pages that I like to have. The home page in English, Japanese and Chinese is hyperlinked to the various pages. Under the product, we should allow the user to select "single sided PCB or double sided PCB". The translation of the contents of the pages with Japanese is not complete but the English and Chinese are complete. You can download the briefing and photos in the dropbox files below;

https://www.filebinvault-example.com/sh/x7k2mq9plw4rt8a/BBQZ_Hn462UdgnRtYmXzzYfLb?dl=0

Target Market(s)

Electronic companies

Industry/Entity Type

Electronic

Coding

Coded - Design and coding required

Number of Pages Required

5+ page

Font styles to use
Sans Serif

Colors
00a990
0353a1
33b8a4

Requirements
Must have
• Get a sense of confidence on our company's integrity and capability to deliver the highest quality PCBs with the most competitive prices and best services. A sense of elegance is essential as we DON'T treat profits as the number one goal. Our number goal is to do the RIGHT things right. Having a mixture of our company photos will be appropriate.

```html
<!DOCTYPE html>
<html lang="en">
<head>
<meta charset="utf-8">
<title>KRU Global Limited</title>
<link href="https://fonts.googleapis.com/css2?family=Montserrat:wght@500;600;700&family=Open+Sans:wght@400;600;700&display=swap" rel="stylesheet">
<style>
:root{
  --blue:#0353a1;
  --blue-dark:#03468a;
  --teal:#00a990;
  --teal-light:#33b8a4;
  --ink:#222;
  --muted:#555;
  --grey:#eeeeee;
  --bar:#1f1f1f;
}
*{box-sizing:border-box;margin:0;padding:0}
html,body{width:1200px;height:4235px;overflow:hidden}
body{font-family:"Open Sans",sans-serif;color:var(--ink);background:#fff;position:relative}
.abs{position:absolute}
h2,h3,.nav,.btn{font-family:"Montserrat",sans-serif}

/* header */
.header{left:0;top:0;width:1200px;height:127px;background:#fff}
.brand{left:121px;top:48px;font-family:"Montserrat",sans-serif;font-weight:700;font-size:44px;color:var(--ink);letter-spacing:2px;display:flex;align-items:center;gap:12px}
.brand .mark{width:22px;height:22px;background:var(--teal)}
.brand-tag{left:121px;top:96px;font-size:10px;color:var(--blue);font-weight:600}
.contact-top{top:64px;font-size:13px;display:flex;align-items:center;gap:8px;color:var(--ink);white-space:nowrap}
.contact-top .ic{width:24px;height:24px;border-radius:50%;background:var(--teal);display:flex;align-items:center;justify-content:center;flex:none}
.lang{left:1012px;top:68px;font-size:13px;display:flex;align-items:center;gap:6px}
.lang .flag{width:18px;height:12px;background:#c33;border:1px solid #ccc}

/* nav */
.nav{left:0;top:127px;width:1200px;height:48px;background:var(--blue);display:flex;align-items:center;padding-left:121px}
.nav a{color:#fff;font-size:15px;font-weight:600;text-decoration:none;height:48px;line-height:48px;padding:0 22px}
.nav a.active{background:var(--teal-light)}
.login{left:948px;top:135px;width:133px;height:32px;background:var(--teal);border-radius:16px;color:#fff;font-size:15px;font-weight:600;text-align:center;line-height:32px;font-family:"Montserrat",sans-serif}

/* hero */
.hero{left:0;top:175px;width:1200px;height:559px;background:linear-gradient(120deg,#c9d3dc 0%,#8fa0ad 40%,#b7c2c9 70%,#dfe5e8 100%)}
.arrow{top:430px;width:26px;height:34px;background:rgba(255,255,255,.7);display:flex;align-items:center;justify-content:center}
.form-panel{left:714px;top:268px;width:274px;height:367px;background:rgba(0,169,144,.35)}
.form-panel h3{background:var(--teal);color:#fff;font-size:22px;text-align:center;height:56px;line-height:56px}
.field{margin:12px 14px 0;height:38px;border:1px solid rgba(255,255,255,.8);background:rgba(255,255,255,.15);color:#fff;font-size:14px;padding:8px 10px}
.field.tall{height:80px}
.form-panel .submit{margin:14px 14px 0;height:44px;background:var(--teal);color:#fff;font-family:"Montserrat",sans-serif;font-weight:700;font-size:19px;text-align:center;line-height:44px}
.dots{left:568px;top:762px;display:flex;gap:10px}
.dots span{width:10px;height:10px;border-radius:50%;background:var(--blue)}

/* about */
.about{left:121px;top:815px;width:960px;text-align:center}
.about h2{font-size:31px;font-weight:700;margin-bottom:14px}
.about p{font-size:15px;line-height:1.3;color:var(--ink)}
.btn{display:inline-block;background:var(--blue);color:#fff;font-weight:700;font-size:14px;border-radius:14px;height:28px;line-height:28px;padding:0 28px}

/* single layered */
.single{left:121px;top:1114px;width:480px}
.single h3{font-size:24px;font-weight:600;margin-bottom:10px;white-space:nowrap}
.single p{font-size:15px;line-height:1.25;margin-bottom:14px}
.table{width:480px;border-collapse:separate;border-spacing:0 8px;font-size:14px}
.table th{background:var(--blue);color:#fff;font-family:"Montserrat",sans-serif;text-align:left;font-size:17px;height:48px;padding-left:18px;font-weight:600}
.table th.pc{width:136px;border-left:8px solid #fff}
.table td{height:46px;padding-left:18px;background:#f4f4f4}
.table td.pc{background:var(--grey);border-left:8px solid #fff}
.pcb-photo{left:627px;top:1124px;width:454px;height:373px;background:linear-gradient(135deg,#2f9a3a,#7cd06a 55%,#2a8c36)}

/* double layered band */
.band{left:0;top:1548px;width:1200px;height:401px;background:linear-gradient(90deg,var(--blue-dark),var(--blue) 60%,#0a61b4)}
.factory-photo{left:121px;top:1598px;width:444px;height:351px;background:linear-gradient(160deg,#e6ecef,#a9b8c1 60%,#6e8594)}
.band-text{left:599px;top:1610px;width:482px;color:#fff}
.band-text h3{font-size:24px;font-weight:700;line-height:1.25;margin-bottom:18px}
.band-text p{font-size:14px;font-weight:600;line-height:1.25;margin-bottom:14px}

/* investment */
.invest{left:121px;top:2108px;width:520px}
.invest h3{font-size:25px;font-weight:700;margin-bottom:14px}
.invest p{font-size:14px;line-height:1.3;margin-bottom:16px;color:var(--ink)}
.invest p.lead{font-weight:600;font-size:15px}
.invest p.em{font-style:italic}
.building-photo{left:678px;top:2098px;width:403px;height:322px;background:linear-gradient(180deg,#8dbfe8 0%,#cfe2ef 45%,#d7d9d6 60%,#7d9a6f 100%)}

/* customers */
.customers-title{left:0;top:2498px;width:1200px;text-align:center;font-size:24px;font-weight:700;font-family:"Montserrat",sans-serif}
.logos{left:121px;top:2561px;width:960px;display:flex;gap:8px}
.logos div{flex:1;height:113px;background:#f2f2f2;display:flex;align-items:center;justify-content:center;font-family:"Montserrat",sans-serif;font-weight:700;font-size:20px;color:var(--blue)}

/* news */
.news{left:0;top:2728px;width:1200px;height:520px;background:var(--blue)}
.news h2{position:absolute;left:0;top:34px;width:1200px;text-align:center;color:#fff;font-size:26px;font-weight:600}
.news .sub{position:absolute;left:0;top:72px;width:1200px;text-align:center;color:#fff;font-size:13px}
.news-nav{position:absolute;left:1036px;top:34px;display:flex;gap:6px}
.news-nav span{width:20px;height:20px;background:#fff;display:flex;align-items:center;justify-content:center}
.news-nav span.on{background:var(--teal)}
.card{top:2841px;width:317px;height:339px;background:#fff;padding:12px}
.card .photo{height:176px;background:linear-gradient(150deg,#dfe7ea,#9fb0bb 55%,#4f6f86)}
.card .date{position:absolute;left:26px;top:26px;width:34px;height:44px;background:#fff;font-size:11px;text-align:center;font-weight:700;line-height:1.3;padding-top:4px}
.card .title{color:var(--teal);font-weight:700;font-size:13px;margin-top:10px}
.card .meta{font-size:12px;color:var(--muted);display:flex;justify-content:space-between;margin-top:2px}
.card p{font-size:13px;line-height:1.3;margin-top:8px}
.card .more{font-size:13px;color:var(--muted);margin-top:6px}
.view-more{left:528px;top:3296px;width:143px;height:30px;background:var(--blue);color:#fff;font-family:"Montserrat",sans-serif;font-weight:700;font-size:14px;text-align:center;line-height:30px;border-radius:15px}

/* contact */
.contact{left:121px;top:3392px;width:450px}
.contact h3{font-size:25px;font-weight:700;margin-bottom:8px}
.contact p{font-size:13px;font-weight:600;line-height:1.3;margin-bottom:10px}
.cfield{height:44px;background:#f4f4f4;font-size:12px;color:var(--muted);padding:14px 12px;margin-bottom:10px}
.cfield.tall{height:112px}
.contact .btn{margin-top:6px;padding:0 36px}
.tiles{left:621px;top:3383px;width:458px;display:grid;grid-template-columns:225px 225px;gap:8px}
.tile{height:210px;display:flex;flex-direction:column;align-items:center;justify-content:center;color:#fff;font-family:"Montserrat",sans-serif;font-size:14px;font-weight:500;text-align:center;line-height:1.25}
.tile svg{margin-bottom:14px}
.tile.blue{background:var(--blue)}
.tile.teal{background:var(--teal-light)}

/* footer */
.footer{left:0;top:3897px;width:1200px;height:282px;background:var(--blue);color:#fff}
.footer .flogo{position:absolute;left:121px;top:30px;font-family:"Montserrat",sans-serif;font-weight:700;font-size:44px;color:#fff;display:flex;align-items:center;gap:12px}
.footer .flogo .mark{width:22px;height:22px;background:var(--teal-light)}
.footer .about-f{position:absolute;left:121px;top:120px;width:230px;font-size:13px;line-height:1.3}
.footer h4{font-family:"Montserrat",sans-serif;font-size:14px;font-weight:700;margin-bottom:14px}
.col{position:absolute;top:48px;font-size:13px}
.col.address{font-size:12px}
.col ul{list-style:none}
.col li{margin-bottom:8px;display:flex;gap:8px;line-height:1.3}
.subscribe input{width:190px;height:28px;border:0;font-size:12px;padding:0 10px;font-family:"Open Sans",sans-serif}
.subscribe .go{display:inline-block;width:28px;height:28px;background:var(--teal);vertical-align:top}
.copyright{left:0;top:4179px;width:1200px;height:56px;background:var(--bar);color:#fff;font-size:13px;font-weight:600;padding:0 121px;display:flex;align-items:center;justify-content:space-between}
.social{display:flex;gap:8px}
.social span{width:22px;height:22px;border-radius:50%;background:#fff}
</style>
</head>
<body>

<header class="abs header">
  <div class="abs brand"><span class="mark"></span>KRU</div>
  <div class="abs brand-tag">Printed Circuit Boards is Our Business</div>
  <div class="abs contact-top" style="left:586px">
    <span class="ic"><svg width="12" height="10" viewBox="0 0 12 10"><rect x="0.5" y="0.5" width="11" height="9" fill="none" stroke="#fff"/><path d="M1 1l5 4 5-4" fill="none" stroke="#fff"/></svg></span>sales@krucircuit-example.com
  </div>
  <div class="abs contact-top" style="left:858px">
    <span class="ic"><svg width="12" height="12" viewBox="0 0 12 12"><path d="M2 1l2 0 1 3-1.5 1a7 7 0 0 0 3.5 3.5L8 7l3 1v2a1 1 0 0 1-1 1A9 9 0 0 1 1 2a1 1 0 0 1 1-1z" fill="#fff"/></svg></span>(852) 2000 1234
  </div>
  <div class="abs lang"><span class="flag"></span>Eng ▾</div>
</header>

<nav class="abs nav">
  <a class="active">HOME</a><a>PRODUCTS</a><a>TECHNICAL CAPABILITIES</a><a>NEWS</a>
</nav>
<div class="abs login">LOGIN</div>

<section class="abs hero" role="img" aria-label="Photo of a technician operating a PCB production line in the factory"></section>
<div class="abs arrow" style="left:44px"><svg width="10" height="14"><path d="M8 1L2 7l6 6" fill="none" stroke="#555" stroke-width="2"/></svg></div>
<div class="abs arrow" style="left:1128px"><svg width="10" height="14"><path d="M2 1l6 6-6 6" fill="none" stroke="#555" stroke-width="2"/></svg></div>
<form class="abs form-panel">
  <h3>CONTACT US</h3>
  <div class="field">Name</div>
  <div class="field">Email</div>
  <div class="field">Phone</div>
  <div class="field tall">Massage</div>
  <div class="submit">Submit</div>
</form>
<div class="abs dots"><span></span><span></span><span></span><span></span></div>

<section class="abs about">
  <h2>KRU GLOBAL LIMITED</h2>
  <p>Established in 2007, KRU Global Limited (KRU) is a Hong Kong company specializing in single and double sized printed circuit boards. Its manufacturing facility is located in a self-owned facility in Lianhe, Huizhou of China which is 50 minutes from Hong Kong.<br>Our mission is to become a premium low costs PCB supplier that fully embraces human, social and environmental responsibilities. Through our insatiable drive to maximize efficiency, KRU is becoming a highly efficient PCB factory with a capacity of 140,000 square meter a month. PCB is our business and it is through continued automation and innovation that will drive our growth in the next 10 years.</p>
  <div class="btn" style="margin-top:16px">Read More</div>
</section>

<section class="abs single">
  <h3>Single Layered Printed Circuit Boards</h3>
  <p>We are offering single layered circuit boards through our own production facility in China for customers in the following industries:</p>
  <table class="table">
    <tr><th>Application</th><th class="pc">Percent%</th></tr>
    <tr><td>Household appliances</td><td class="pc">60%</td></tr>
    <tr><td>Power supply</td><td class="pc">20%</td></tr>
    <tr><td>Lighting control system</td><td class="pc">10%</td></tr>
    <tr><td>others</td><td class="pc">10%</td></tr>
  </table>
</section>
<div class="abs pcb-photo" role="img" aria-label="Close-up photo of a green printed circuit board"></div>

<section class="abs band"></section>
<div class="abs factory-photo" role="img" aria-label="Photo of a PCB assembly machine inside the factory"></div>
<div class="abs band-text">
  <h3>DOUBLE LAYERED AND MULTI-LAYERED PRINTED CIRCUIT BOARDS</h3>
  <p>We are offering two layered and multi-layered circuit boards for our customers through our strategically approved printed circuit boards manufacturers.With our own UL for double sided and multi-layered circuit boards, we work with a number of strategically approved manufacturers in delivering 100% quality guaranteed printed circuit boards for our customers.</p>
  <p>We perform comprehensive quality and environmental audit of our manufacturers on quarterly and annual basis.</p>
  <p>Technical capability of our double sided/multi layered PCBs facility</p>
</div>

<section class="abs invest">
  <h3>OUR INVESTMENT AND UPGRADE</h3>
  <p class="lead">Maintaining a highly automated factory is the only way to ensure consistent product and long term competitive efficiency.</p>
  <p class="em">From 2015 to 2017, KRU invested over US$3.5 million in automating our production and quality control process and enhancing our environmental processing facility. We will spend a further US$1.5 million in 2018 to continue our improvement process to ensure we are one of the most efficient and highest quality single sided PCB manufacturers in Asia. By the end of 2018, 100% of our PCBs will be inspected by AVI before they are delivered to our customers.</p>
  <div class="btn">Read More</div>
</section>
<div class="abs building-photo" role="img" aria-label="Photo of the factory building exterior under blue sky"></div>

<h2 class="abs customers-title">OUR CUSTOMERS</h2>
<div class="abs logos">
  <div>ORIONEX</div><div>Kelvara</div><div>TAKEMI</div><div>NORDEL</div><div>VANTRO</div><div>Lumixa</div>
</div>

<section class="abs news">
  <h2>NEWS</h2>
  <div class="sub">Lorem Ipsum is simply dummy text.</div>
  <div class="news-nav"><span><svg width="8" height="10"><path d="M6 1L2 5l4 4" fill="none" stroke="#0353a1" stroke-width="2"/></svg></span><span class="on"><svg width="8" height="10"><path d="M2 1l4 4-4 4" fill="none" stroke="#fff" stroke-width="2"/></svg></span></div>
</section>
<article class="abs card" style="left:107px">
  <div class="photo" role="img" aria-label="Photo of factory workers at a production station"></div>
  <div class="date">24<br>Feb</div>
  <div class="title">POST TITLE</div>
  <div class="meta"><span>▦ February 24, 2018</span><span>♡ 20 &nbsp;▢ 12</span></div>
  <p>Lorem Ipsum is simply dummy text of the And printing matter and typesetting industry.</p>
  <div class="more">Read More..⊙</div>
</article>
<article class="abs card" style="left:446px">
  <div class="photo" role="img" aria-label="Photo of a PCB manufacturing machine line"></div>
  <div class="date">26<br>Feb</div>
  <div class="title">POST TITLE</div>
  <div class="meta"><span>▦ February 26, 2018</span><span>♡ 20 &nbsp;▢ 12</span></div>
  <p>Lorem Ipsum is simply dummy text of the printing and typesetting industry.</p>
  <div class="more">Read More..⊙</div>
</article>
<article class="abs card" style="left:779px">
  <div class="photo" role="img" aria-label="Photo of the factory inspection area"></div>
  <div class="date">07<br>Feb</div>
  <div class="title">POST TITLE</div>
  <div class="meta"><span>▦ February 07, 2018</span><span>♡ 20 &nbsp;▢ 12</span></div>
  <p>Lorem Ipsum is simply dummy text of the printing and typesetting industry.</p>
  <div class="more">Read More..⊙</div>
</article>
<div class="abs view-more">View More</div>

<section class="abs contact">
  <h3>CONTACT US</h3>
  <p>Please fill out this quick contact form and someone will be in touch with you shortly</p>
  <div class="cfield">Name*</div>
  <div class="cfield">Phone*</div>
  <div class="cfield">Email*</div>
  <div class="cfield tall">Message</div>
  <div class="btn">SUBMIT</div>
</section>
<div class="abs tiles">
  <div class="tile blue">
    <svg width="60" height="66" viewBox="0 0 60 66" fill="none" stroke="#fff" stroke-width="3"><circle cx="30" cy="26" r="20"/><circle cx="30" cy="26" r="11"/><path d="M18 42l-6 20 10-5 5 8 3-19M42 42l6 20-10-5-5 8-3-19"/></svg>
    EXCELLENCE<br>IN QUALITY
  </div>
  <div class="tile teal">
    <svg width="56" height="66" viewBox="0 0 56 66" fill="none" stroke="#fff" stroke-width="3"><path d="M6 4h44v36L28 62 6 40z"/><path d="M28 14v26M20 32l8 9 8-9"/><path d="M22 20h10"/></svg>
    EXCELLENCE<br>IN PRICES
  </div>
  <div class="tile teal">
    <svg width="64" height="64" viewBox="0 0 64 64" fill="none" stroke="#fff" stroke-width="3"><circle cx="32" cy="32" r="10"/><path d="M32 4v10M32 50v10M4 32h10M50 32h10M12 12l7 7M45 45l7 7M52 12l-7 7M19 45l-7 7"/><circle cx="32" cy="32" r="20"/></svg>
    EXCELLENCE<br>IN SERVICES
  </div>
  <div class="tile teal">
    <svg width="64" height="64" viewBox="0 0 64 64" fill="none" stroke="#fff" stroke-width="3"><circle cx="32" cy="32" r="26"/><path d="M20 32l9 9 16-18"/></svg>
    EXCELLENCE<br>IN ON TIME DELIVERY
  </div>
</div>

<footer class="abs footer">
  <div class="flogo"><span class="mark"></span>KRU</div>
  <div class="about-f">Lorem Ipsum is simply dummy text of the printing and typesetting industry. Lorem Ipsum has been the industry's standard.<br><b>Read More ⊙</b></div>
  <div class="col" style="left:401px">
    <h4>QUICK LINKS</h4>
    <ul><li>› Home</li><li>› Products</li><li>› Technical Capabilities</li><li>› News</li><li>› Contact Us</li></ul>
  </div>
  <div class="col address" style="left:600px;width:240px">
    <h4>HONG KONG</h4>
    <ul>
      <li><svg width="10" height="14" viewBox="0 0 10 14"><path d="M5 0a5 5 0 0 1 5 5c0 4-5 9-5 9S0 9 0 5a5 5 0 0 1 5-5z" fill="#fff"/></svg><span>KRU Global Limited<br>18/F Harbour Point 21 Marine Road<br>Wan Chai</span></li>
      <li>☏ <span>Tel: +852-20001234</span></li>
      <li>⎙ <span>Fax: +852-20005678</span></li>
      <li>✉ <span>Email: sales@krucircuit-example.com</span></li>
    </ul>
  </div>
  <div class="col subscribe" style="left:861px;width:220px">
    <h4>SUBSCRIBE</h4>
    <p style="line-height:1.3;margin-bottom:14px">Get the latest updates and offer Lorem Ipsum is simply dummy text of the printing.</p>
    <input type="text" value="Enter Your Email"><span class="go"></span>
  </div>
</footer>
<div class="abs copyright">
  <span>© 2018 KRU - ALL RIGHTS RESERVED</span>
  <div class="social"><span></span><span></span><span></span><span></span><span></span></div>
</div>

</body>
</html>
```